Kestrel Roadway Wheels

I need a wrap designed for a box truck. The company is a mobile tire shop. It’s a tire shop on wheels, that comes anywhere you are to service your tires.

```html
<!DOCTYPE html>
<html lang="en">
<head>
<meta charset="utf-8">
<title>Kestrel Roadway Wheels – Box Truck Wrap</title>
<link rel="stylesheet" href="https://fonts.googleapis.com/css2?family=Roboto:wght@500&family=Montserrat:ital,wght@1,800;1,900&family=Lato:wght@700&display=swap">
<style>
  :root {
    --page-bg: #f0f0f0;
    --wrap-black: #0b0c0e;
    --wrap-charcoal: #2a2c30;
    --sky-blue: #2fa7df;
    --navy: #0d4f86;
    --deep-navy: #0a2c4f;
    --white: #ffffff;
    --tire-black: #141518;
    --rim-silver: #7d8085;
  }
  * { margin: 0; padding: 0; box-sizing: border-box; }
  html, body {
    width: 1200px; height: 1200px; overflow: hidden;
    background: var(--page-bg);
  }
  .canvas { position: relative; width: 1200px; height: 1200px; }
  .wrap-panel {
    position: absolute; left: 100px; top: 57px;
    width: 1000px; height: 556px; overflow: hidden;
    background: radial-gradient(ellipse at 35% 40%, var(--wrap-charcoal) 0%, var(--wrap-black) 70%);
    box-shadow: 0 14px 22px rgba(0,0,0,0.18);
  }
  .wrap-swoosh { position: absolute; inset: 0; }
  .brand-name {
    position: absolute; right: 80px; top: 58px;
    font-family: 'Lato', sans-serif; font-weight: 700;
    font-size: 70px; line-height: 80px; color: var(--white);
    text-align: right; white-space: nowrap;
  }
  .tire-stack {
    position: absolute; left: 6px; top: 214px; width: 384px; height: 336px;
    border-radius: 14px;
    background:
      radial-gradient(ellipse at 62% 48%, var(--rim-silver) 0%, #3a3c40 38%, transparent 62%),
      linear-gradient(160deg, #26282c 0%, var(--tire-black) 60%, #0e0f11 100%);
  }
  .service-list {
    position: absolute; left: 430px; top: 272px; list-style: none;
    font-family: 'Roboto', sans-serif; font-weight: 500;
    font-size: 20.5px; color: var(--white); line-height: 28px;
    text-transform: uppercase;
  }
  .service-list li { display: flex; align-items: center; }
  .service-list li::before {
    content: ""; width: 7px; height: 7px; border-radius: 50%;
    background: var(--sky-blue); margin-right: 12px;
  }
  .call-line {
    position: absolute; right: 28px; top: 460px;
    font-family: 'Montserrat', sans-serif; font-style: italic; font-weight: 800;
    font-size: 16px; color: var(--deep-navy);
  }
  .call-line strong { font-weight: 900; font-size: 18px; }
  .phone {
    position: absolute; right: 28px; top: 478px;
    font-family: 'Montserrat', sans-serif; font-style: italic; font-weight: 900;
    font-size: 54px; color: var(--white); letter-spacing: 0.5px;
    text-shadow: 2px 3px 0 rgba(0,0,0,0.45);
  }
</style>
</head>
<body>
<div class="canvas">
  <section class="wrap-panel">
    <svg class="wrap-swoosh" viewBox="0 0 1000 556" width="1000" height="556" aria-hidden="true">
      <path d="M0 380 C 200 470 420 470 620 420 C 780 380 900 320 1000 290 L1000 556 L0 556 Z" fill="var(--navy)"/>
      <path d="M0 395 C 200 490 420 480 620 438 C 780 405 900 370 1000 360 L1000 556 L0 556 Z" fill="var(--wrap-black)"/>
      <path d="M0 405 C 220 505 430 490 620 452 C 780 420 900 405 1000 402 L1000 556 L0 556 Z" fill="var(--sky-blue)"/>
    </svg>

    <h1 class="brand-name">Kestrel Roadway<br>Wheels</h1>

    <div class="tire-stack" role="img" aria-label="Stack of black tires mounted on silver alloy wheels"></div>

    <ul class="service-list">
      <li>Low profile tires &amp; custom wheels</li>
      <li>Tire mounting &amp; installation</li>
      <li>Emergency roadside service</li>
      <li>New &amp; used tires</li>
      <li>Tire repairs</li>
    </ul>

    <p class="call-line">Call us &amp; <strong>WE COME TO YOU!</strong></p>
    <p class="phone">555.014.0199</p>
  </section>
</div>
</body>
</html>
```